Nuvrik: Law Flyer

We need an A5 double sided leaflet that is not too congested with writing but gets all the necessary information across.

We want the leaflet to look clean and professional but also colourful and something that entices people to read it.

The message we want to subtly convey is that knowledge is power and Nuvrik:Law is the fountain to their legal knowledge. Or alternatively Nuvrik:Law is like a filter that sucks in all the legal jargon typically used by lawyers and produces easy to digest and understandable information.

Our slogan is Nuvrik:Law... We teach to uplift.
Please feel free to visit our site www.NuvrikLaw.co.uk for more information on what we do or to gain inspiration from the site to ensure both the leaflet and site complement one another.

With that being said, please feel free to be as creative as you please.

Target Market(s)

People who have no legal knowledge. Our core audience are 25-35 years old while our subsidiary audience are 18 - 25 years old.

Industry/Entity Type

Legal

Requirements
Must have
• Our Logo
Our facebook : www.palwall.net/NuvrikLaw
Our twtter: @NuvrikLaw
Our website www.NuvrikLaw.co.uk
Nice to have
• Some nice creative illustrations.
Should not have
• Boring typical law related photographs.

```html
<!DOCTYPE html>
<html lang="en">
<head>
<meta charset="utf-8">
<title>Nuvrik:Law – Bridging the gap</title>
<link rel="stylesheet" href="https://fonts.googleapis.com/css2?family=Archivo+Black&family=Tinos:wght@400;700&display=swap">
<style>
  :root {
    --slate: #656d70;
    --slate-dark: #575e61;
    --yellow: #f4ec1c;
    --white: #ffffff;
    --red: #d0152c;
    --pink: #d6245a;
    --ink: #222222;
    --link: #1c2f9c;
    --icon: #3b5a9c;
    --icon-alt: #3aa0d8;
  }
  * { margin: 0; padding: 0; box-sizing: border-box; }
  html, body { width: 846px; height: 1200px; overflow: hidden; background: var(--white); }
  .flyer { position: relative; width: 846px; height: 1200px; background: var(--white); overflow: hidden; font-family: "Tinos", serif; }

  .brand { position: absolute; left: 70px; top: 40px; width: 380px; }
  .brand-name { font-family: "Archivo Black", sans-serif; font-size: 62px; line-height: 1; color: var(--slate); letter-spacing: -1px; }
  .brand-rule { height: 2px; background: var(--pink); margin: 22px 0 10px; width: 370px; }
  .brand-tagline { font-family: "Tinos", serif; font-size: 24px; color: var(--slate-dark); padding-left: 95px; }

  .scales-art { position: absolute; left: 592px; top: 22px; width: 238px; height: 212px;
    background: linear-gradient(180deg, #7d8588 0%, #62696c 100%); border-radius: 4px; }

  .social-bar { position: absolute; left: 0; top: 240px; width: 846px; height: 52px; background: #e8e9e9; }
  .social-item { position: absolute; top: 8px; height: 36px; display: flex; align-items: center; }
  .social-icon { width: 36px; height: 36px; border-radius: 4px; background: var(--icon); }
  .social-icon.alt { background: var(--icon-alt); }
  .social-label { height: 36px; margin-left: 5px; padding: 0 10px; background: var(--slate); color: var(--white);
    font-size: 21px; display: flex; align-items: center; }
  .social-site { position: absolute; left: 592px; top: 8px; height: 36px; padding: 0 8px; background: var(--white);
    font-size: 21px; color: var(--ink); display: flex; align-items: center; }

  .hero { position: absolute; left: 0; top: 298px; width: 846px; height: 660px; }
  .hero-band { position: absolute; background: var(--slate); }
  .hero-band.top { left: 0; top: 0; width: 846px; height: 362px; }
  .hero-band.lower { left: 40px; top: 362px; width: 806px; height: 298px; }

  .headline { position: absolute; font-family: "Archivo Black", sans-serif; white-space: nowrap; line-height: 1; }
  .headline.yellow { color: var(--yellow); text-shadow: 3px 3px 0 #1d1d1d; }
  .headline.white { color: var(--white); text-shadow: 3px 3px 0 #1d1d1d; }
  .h-bridging { left: 58px; top: 70px; font-size: 104px; letter-spacing: 4px; }
  .h-gap { left: 350px; top: 190px; font-size: 150px; color: var(--white); letter-spacing: 12px;
    -webkit-text-stroke: 5px var(--red); paint-order: stroke fill; }
  .h-between { left: 66px; top: 372px; font-size: 40px; letter-spacing: 3px; }
  .h-english { left: 200px; top: 452px; font-size: 58px; letter-spacing: 3px; }
  .h-welsh { left: 136px; top: 558px; font-size: 48px; letter-spacing: 2.5px; }

  .officer-art { position: absolute; left: 35px; top: 965px; width: 240px; height: 200px;
    background: linear-gradient(160deg, #d9dde8 0%, #9aa6c6 100%); border-radius: 4px; }

  .feature-title { position: absolute; left: 456px; top: 952px; font-size: 44px; font-weight: 700; color: var(--red); }
  .feature-text { position: absolute; left: 282px; top: 1011px; width: 554px; font-size: 24px; line-height: 1.5;
    color: var(--ink); text-align: justify; text-indent: 30px; letter-spacing: 0.3px; }
  .feature-cta { position: absolute; left: 336px; top: 1152px; font-size: 20px; color: var(--red); }
  .feature-link { position: absolute; left: 530px; top: 1152px; font-size: 20px; color: var(--ink); }
  .feature-link span { color: var(--link); }

  .footer-band { position: absolute; left: 0; top: 1190px; width: 846px; height: 10px; background: var(--slate); }
</style>
</head>
<body>
<main class="flyer">
  <header class="brand">
    <div class="brand-name">Nuvrik:Law</div>
    <div class="brand-rule"></div>
    <div class="brand-tagline">We teach to uplift</div>
  </header>
  <div class="scales-art" role="img" aria-label="Illustration of the scales of justice"></div>

  <nav class="social-bar">
    <div class="social-item" style="left:12px"><div class="social-icon"></div><div class="social-label">www.palwall.net/NuvrikLaw</div></div>
    <div class="social-item" style="left:378px"><div class="social-icon alt"></div><div class="social-label">@NuvrikLaw</div></div>
    <div class="social-site">www.NuvrikLaw.co.uk</div>
  </nav>

  <section class="hero">
    <div class="hero-band top"></div>
    <div class="hero-band lower"></div>
    <h1>
      <span class="headline yellow h-bridging">Bridging the</span>
      <span class="headline h-gap">gap</span>
      <span class="headline yellow h-between">between the average citizen</span>
      <span class="headline white h-english">and the English</span>
      <span class="headline yellow h-welsh">and Welsh legal system.</span>
    </h1>
  </section>

  <div class="officer-art" role="img" aria-label="Cartoon police officer shouting STOP through a megaphone"></div>
  <h2 class="feature-title">Stop &amp; Search.</h2>
  <p class="feature-text">If a police officer attempted to stop and search you, would you know exactly what it is that the law allows for them to do? No?</p>
  <p class="feature-cta">Want to Know...</p>
  <p class="feature-link">Visit: <span>www.nuvriklaw.co.uk</span></p>

  <div class="footer-band"></div>
</main>
</body>
</html>
```